Kestrel Ridge Hides

I created the attached in quill mark. I would like the background to look like black leather and the text to be gold. Any other suggestions would be appreciated. Thank you
Please note: all text now should be white .... sorry Partners changed their mind
Please remember when submitting designs, this design is for a folded business card with printing on all 4 sides ..... thank you
Also, the front of the card must have the wording above the logo. These will be placed in the wallet ID pockets and I would like to be able to read the wording.
Printing
I would like a folded business card. I created one in Quillmark but don't know how to send it to you to apply the final touches.

```html
<!DOCTYPE html>
<html lang="en">
<head>
<meta charset="utf-8">
<title>Kestrel Ridge Hides – Card Front</title>
<link rel="stylesheet" href="https://fonts.googleapis.com/css2?family=Allerta+Stencil&display=swap">
<style>
  :root {
    --leather-dark: #0e1012;
    --leather-mid: #16181a;
    --band-dark: #181a1b;
    --band-light: #222426;
    --band-edge: #3b3d3f;
    --ink-white: #eef1f0;
  }
  * { margin: 0; padding: 0; box-sizing: border-box; }
  html, body {
    width: 1200px;
    height: 693px;
    overflow: hidden;
    background: var(--leather-dark);
  }
  .card {
    position: relative;
    width: 1200px;
    height: 693px;
    overflow: hidden;
    background:
      radial-gradient(ellipse at 50% 40%, rgba(255,255,255,0.035), transparent 70%),
      linear-gradient(180deg, var(--leather-mid) 0%, var(--leather-dark) 100%);
  }
  .card-headline {
    position: absolute;
    top: 96px;
    left: 0;
    width: 100%;
    text-align: center;
    font-family: "Allerta Stencil", sans-serif;
    font-size: 52px;
    letter-spacing: 0.22em;
    padding-left: 0.22em;
    color: var(--ink-white);
    text-transform: uppercase;
    line-height: 1;
  }
  .logo-band {
    position: absolute;
    top: 315px;
    left: 0;
    width: 100%;
    height: 257px;
    background:
      radial-gradient(ellipse at 50% 50%, var(--band-light), var(--band-dark) 75%);
    border-top: 1px solid var(--band-edge);
    border-bottom: 1px solid var(--band-edge);
    display: flex;
    align-items: center;
    justify-content: center;
  }
  .brand-name {
    font-family: "Allerta Stencil", sans-serif;
    font-size: 26px;
    letter-spacing: 0.12em;
    color: var(--ink-white);
    text-transform: uppercase;
  }
</style>
</head>
<body>
  <main class="card">
    <h1 class="card-headline">100% Kestrel Ridge Hides</h1>
    <section class="logo-band">
      <span class="brand-name">Kestrel Ridge Hides</span>
    </section>
  </main>
</body>
</html>
```